Education related business need name card design

We need name card design for long term study agent.
Company name is Harbor Lantern.
We support clients to connect to the world.
Clients are Japanese family who has primary and secondary school students.

Company Logo is reflection of the globe and HL (Harbor Lantern).
Since business is related to education, we would like to show reliability and love to see the world map (atlas) in the name card.

Target Market(s)

late 30's to 50's parents of primary and secondary students who are enthusiastic for education. Secondary school management

Industry/Entity Type

Education

Contact Information for Business Card

Company name, Address, Official position, Name, Phone number, Mobile number, email address,

Font styles to use
Serif
Other font styles liked:
• Century Gothic(logo)

Requirements
Must have
• Since businee is related to education, we would like to show reliability and love to see the world map (atlas) in the name card.

```html
<!DOCTYPE html>
<html lang="en">
<head>
<meta charset="utf-8">
<title>Harbor Lantern – Business Card</title>
<link rel="stylesheet" href="https://fonts.googleapis.com/css2?family=Lora:wght@400;700&display=swap">
<style>
  :root {
    --stage: #eceef1;
    --brand-blue: #1e80cf;
    --brand-blue-deep: #1569b3;
    --map-light: #5aa8e6;
    --map-mid: #3f96dc;
    --paper: #ffffff;
    --ink-dark: #1d2a3a;
    --text-light: #ffffff;
  }
  html, body {
    margin: 0;
    width: 1200px;
    height: 871px;
    overflow: hidden;
    background: var(--stage);
  }
  .stage {
    width: 1200px;
    height: 871px;
    display: flex;
    align-items: center;
    justify-content: center;
    gap: 40px;
  }
  .card {
    position: relative;
    width: 540px;
    height: 310px;
    overflow: hidden;
    box-shadow: 0 6px 18px rgba(0,0,0,0.18);
    font-family: "Lora", serif;
  }

  /* Front side */
  .card--front { background: var(--brand-blue); }
  .atlas {
    position: absolute;
    left: 30px;
    top: 70px;
    width: 480px;
    height: 220px;
    border-radius: 40px;
    background: radial-gradient(ellipse at 50% 50%, var(--map-light) 0%, var(--map-mid) 55%, var(--brand-blue) 100%);
  }
  .front-name {
    position: absolute;
    top: 22px;
    left: 28px;
    margin: 0;
    color: var(--text-light);
    font-size: 30px;
    font-weight: 400;
    letter-spacing: 0.3px;
  }
  .front-dot {
    position: absolute;
    left: 50%;
    top: 178px;
    width: 110px;
    height: 110px;
    margin: -55px 0 0 -55px;
    border-radius: 50%;
    background: var(--text-light);
  }

  /* Back side */
  .card--back { background: var(--paper); }
  .back-brand {
    position: absolute;
    top: 24px;
    left: 28px;
    display: flex;
    align-items: center;
    gap: 12px;
  }
  .back-dot {
    width: 38px;
    height: 38px;
    border-radius: 50%;
    background: var(--brand-blue);
    flex: none;
  }
  .back-brand .brand-name {
    color: var(--brand-blue-deep);
    font-size: 18px;
    line-height: 1.15;
  }
  .holder {
    position: absolute;
    top: 92px;
    left: 28px;
  }
  .holder-name {
    margin: 0;
    font-weight: 700;
    font-size: 24px;
    color: var(--brand-blue);
  }
  .holder-title {
    margin: 4px 0 0;
    font-weight: 700;
    font-size: 11px;
    color: var(--ink-dark);
    letter-spacing: 0.6px;
  }
  .contact-band {
    position: absolute;
    left: 0;
    bottom: 0;
    width: 330px;
    height: 124px;
    background: var(--brand-blue);
    padding: 16px 28px;
    box-sizing: border-box;
  }
  .contact-list {
    margin: 0;
    padding: 0;
    list-style: none;
    color: var(--text-light);
    font-size: 12px;
    line-height: 1.7;
    white-space: nowrap;
  }
  .accent-block {
    position: absolute;
    right: 0;
    bottom: 0;
    width: 210px;
    height: 124px;
  }
</style>
</head>
<body>
<main class="stage">

  <section class="card card--front" aria-label="Business card front">
    <div class="atlas" role="img" aria-label="Faint world map across the card"></div>
    <p class="front-name">Harbor Lantern Pte.Ltd.</p>
    <span class="front-dot"></span>
  </section>

  <section class="card card--back" aria-label="Business card back">
    <div class="back-brand">
      <span class="back-dot"></span>
      <span class="brand-name">Harbor Lantern<br>Pte.Ltd.</span>
    </div>
    <div class="holder">
      <p class="holder-name">Lorem Ipsum Dolor</p>
      <p class="holder-title">POSITION HERE</p>
    </div>
    <div class="contact-band">
      <ul class="contact-list">
        <li>Address: Lorem Ipsum Dolor</li>
        <li>Phone No: 555 014 277</li>
        <li>Email: hello@harborlantern-mail.com</li>
        <li>Website: www.harborlantern-study.com</li>
      </ul>
    </div>
    <svg class="accent-block" viewBox="0 0 210 124" aria-hidden="true">
      <polygon points="0,124 0,40 210,0 210,124" fill="var(--brand-blue)"/>
      <rect x="0" y="62" width="210" height="6" fill="var(--paper)"/>
      <rect x="0" y="90" width="210" height="6" fill="var(--paper)"/>
    </svg>
  </section>

</main>
</body>
</html>
```